Brightmoor Solar Panels

We are looking for a design that will represent keeping solar panels clean or an easier way in which to clean solar panels. During operation, a solar panel´s efficiency is reduced by the fact that dirt deposits on the surface of the panels. The type of dirt depends on climate conditions and location, ranging from dust soiling, biological soiling (biofilms, algaeās), and/or bird droppings: The winning design will be turned into a 4" x 4" sticker for internal company use.

```html
<!DOCTYPE html>
<html lang="en">
<head>
<meta charset="utf-8">
<title>Brightmoor Solar Panels – Clean Panels Sticker</title>
<link rel="stylesheet" href="https://fonts.googleapis.com/css2?family=Montserrat:wght@600&display=swap">
<style>
  :root {
    --page: #ffffff;
    --ring: #ececec;
    --blue: #0a14a0;
    --green: #069a07;
    --white: #ffffff;
  }
  html, body {
    margin: 0;
    padding: 0;
    width: 1200px;
    height: 1200px;
    overflow: hidden;
    background: var(--page);
    font-family: "Montserrat", sans-serif;
  }
  .sticker {
    display: block;
    width: 1200px;
    height: 1200px;
  }
  .outer-ring { fill: var(--ring); }
  .quadrant-blue { fill: var(--blue); }
  .quadrant-green { fill: var(--green); }
  .divider { stroke: var(--white); stroke-width: 13; }
  .center-frame { fill: var(--white); }
  .line-icon { fill: none; stroke: var(--white); stroke-width: 9; stroke-linecap: round; stroke-linejoin: round; }
  .dust-outline { fill: none; stroke: var(--white); stroke-width: 9; stroke-linecap: round; stroke-linejoin: round; }
  .dust-speck { fill: var(--white); }
  .battery-cell { fill: none; stroke: var(--white); stroke-width: 6; }
  .algae-spot { fill: url(#algae-glow); stroke: var(--white); stroke-width: 3; }
  .bulb-glass { fill: url(#bulb-glow); }
</style>
</head>
<body>
<svg class="sticker" viewBox="0 0 1200 1200" xmlns="http://www.w3.org/2000/svg">
  <defs>
    <radialGradient id="algae-glow">
      <stop offset="0" stop-color="#069a07"/>
      <stop offset="0.55" stop-color="#9fd79f"/>
      <stop offset="1" stop-color="#ffffff"/>
    </radialGradient>
    <radialGradient id="bulb-glow">
      <stop offset="0" stop-color="#069a07"/>
      <stop offset="0.6" stop-color="#a9dba9"/>
      <stop offset="1" stop-color="#ffffff"/>
    </radialGradient>
    <linearGradient id="panel-tone" x1="0" y1="0" x2="1" y2="1">
      <stop offset="0" stop-color="#b9dcf5"/>
      <stop offset="0.5" stop-color="#5d9fd8"/>
      <stop offset="1" stop-color="#1d5fa8"/>
    </linearGradient>
    <radialGradient id="bird-tone">
      <stop offset="0" stop-color="#e6e8fa"/>
      <stop offset="0.5" stop-color="#9aa0e4"/>
      <stop offset="1" stop-color="#0a14a0"/>
    </radialGradient>
    <clipPath id="disc-clip"><circle cx="600" cy="600" r="540"/></clipPath>
  </defs>

  <!-- Outer ring -->
  <circle class="outer-ring" cx="600" cy="600" r="567"/>

  <!-- Four soiling quadrants -->
  <g class="quadrants" clip-path="url(#disc-clip)">
    <rect class="quadrant-blue" x="0" y="0" width="600" height="600"/>
    <rect class="quadrant-green" x="600" y="0" width="600" height="600"/>
    <rect class="quadrant-green" x="0" y="600" width="600" height="600"/>
    <rect class="quadrant-blue" x="600" y="600" width="600" height="600"/>
    <line class="divider" x1="600" y1="0" x2="600" y2="1200"/>
    <line class="divider" x1="0" y1="600" x2="1200" y2="600"/>
  </g>

  <!-- Bird droppings -->
  <ellipse class="bird-area" cx="315" cy="330" rx="150" ry="125" fill="url(#bird-tone)" role="img" aria-label="White line drawing of a perched bird with a dropping beneath it"/>

  <!-- Biological soiling -->
  <g class="algae" role="img" aria-label="Spots of algae and biofilm">
    <ellipse class="algae-spot" cx="831" cy="257" rx="53" ry="37"/>
    <ellipse class="algae-spot" cx="947" cy="291" rx="37" ry="27"/>
    <ellipse class="algae-spot" cx="800" cy="337" rx="51" ry="27"/>
    <ellipse class="algae-spot" cx="911" cy="357" rx="43" ry="33"/>
    <ellipse class="algae-spot" cx="853" cy="407" rx="36" ry="27"/>
  </g>

  <!-- Dust soiling -->
  <g class="dust" role="img" aria-label="Dust cloud">
    <path class="dust-outline" d="M790 905 a48 48 0 0 1 5 -90 a62 62 0 0 1 105 -50 a55 55 0 0 1 85 60 a50 50 0 0 1 -5 90 a58 58 0 0 1 -85 45 a60 60 0 0 1 -105 -55 z"/>
    <path class="dust-outline" d="M800 815 q-30 -5 -60 20 q-20 30 5 55 q-15 30 10 45"/>
    <path class="dust-outline" d="M970 800 q25 -5 30 25 q20 25 -5 55"/>
    <path class="dust-outline" d="M830 985 q5 20 30 18 q25 5 35 -15"/>
    <path class="dust-outline" d="M870 745 q15 -20 40 -10 q20 -15 35 5"/>
    <circle class="dust-speck" cx="835" cy="820" r="6"/>
    <circle class="dust-speck" cx="860" cy="805" r="5"/>
    <circle class="dust-speck" cx="905" cy="790" r="6"/>
    <circle class="dust-speck" cx="940" cy="830" r="5"/>
    <circle class="dust-speck" cx="960" cy="865" r="6"/>
    <circle class="dust-speck" cx="815" cy="880" r="5"/>
    <circle class="dust-speck" cx="850" cy="930" r="6"/>
    <circle class="dust-speck" cx="880" cy="945" r="5"/>
    <circle class="dust-speck" cx="940" cy="920" r="6"/>
    <circle class="dust-speck" cx="900" cy="880" r="4"/>
  </g>

  <!-- Energy output: bulb and battery -->
  <g class="energy">
    <g class="bulb">
      <path class="bulb-glass" d="M276 757 a64 64 0 0 1 40 114 q-8 8 -8 22 h-64 q0 -14 -8 -22 a64 64 0 0 1 40 -114 z"/>
      <line class="line-icon" x1="246" y1="915" x2="306" y2="915"/>
      <line class="line-icon" x1="246" y1="935" x2="306" y2="935"/>
      <line class="line-icon" x1="256" y1="955" x2="296" y2="955"/>
      <line class="line-icon" x1="276" y1="702" x2="276" y2="727"/>
      <line class="line-icon" x1="206" y1="728" x2="222" y2="746"/>
      <line class="line-icon" x1="346" y1="728" x2="330" y2="746"/>
      <line class="line-icon" x1="176" y1="795" x2="200" y2="797"/>
      <line class="line-icon" x1="376" y1="795" x2="352" y2="797"/>
      <line class="line-icon" x1="186" y1="858" x2="206" y2="846"/>
      <line class="line-icon" x1="366" y1="858" x2="346" y2="846"/>
    </g>
    <g class="battery">
      <rect x="467" y="857" width="44" height="18" rx="3" fill="var(--white)"/>
      <rect class="line-icon" x="431" y="875" width="116" height="214" rx="12"/>
      <rect class="battery-cell" x="448" y="894" width="82" height="26"/>
      <rect class="battery-cell" x="448" y="932" width="82" height="26"/>
      <rect class="battery-cell" x="448" y="970" width="82" height="26"/>
      <rect class="battery-cell" x="448" y="1008" width="82" height="26"/>
      <rect class="battery-cell" x="448" y="1046" width="82" height="26"/>
    </g>
  </g>

  <!-- Center: cleaning the panel -->
  <circle class="center-frame" cx="600" cy="600" r="250"/>
  <circle cx="600" cy="600" r="236" fill="url(#panel-tone)" role="img" aria-label="Photo of a blue squeegee cleaning a solar panel"/>
</svg>
</body>
</html>
```